Redesign Powerpoint presentation

Attached is a presentation which needs to be redesigned and made to look more cool and slick.
Reason: Am extending the deadline as I have not recived enough designs that meet my expectations .
Marketing heads and managers .All people intersted in sales promotions

```html
<!DOCTYPE html>
<html lang="en">
<head>
<meta charset="utf-8">
<title>Rewardnest – Presentation Slides</title>
<link href="https://fonts.googleapis.com/css2?family=Open+Sans:wght@400;600;700&display=swap" rel="stylesheet">
<style>
:root{
  --bg:#efe9e1;
  --green-dark:#1d5a45;
  --green:#3f8a4a;
  --green-text:#2e7d3a;
  --green-pale:#b4d2ae;
  --arrow-grey:#8a9a92;
  --purple:#6b3f95;
  --purple-mid:#9b7ac0;
  --purple-light:#e6dcf1;
  --ink:#444;
  --white:#fff;
  --chrome:#dfe3e8;
  --teal:#2f7f86;
  --yellow-pale:#f2f3c2;
}
*{box-sizing:border-box;margin:0;padding:0}
html,body{width:1200px;height:960px;overflow:hidden}
body{background:var(--bg);font-family:"Open Sans",Arial,sans-serif;color:var(--ink);position:relative}
.slide{position:absolute;width:208px;height:157px;background:var(--white);overflow:hidden;box-shadow:0 1px 3px rgba(0,0,0,.18)}
.c1{left:44px}.c2{left:270px}.c3{left:496px}.c4{left:722px}.c5{left:948px}
.r1{top:145px}.r2{top:316px}.r3{top:487px}.r4{top:658px}
.band{position:absolute;left:0;top:0;width:208px;height:157px}
.swoosh{position:absolute;left:86px;top:92px;width:122px;height:44px;border-radius:50% 50% 0 0;background:radial-gradient(ellipse at 35% 60%,rgba(138,154,146,.55),rgba(180,210,174,.35) 55%,rgba(255,255,255,0) 75%)}
.url{position:absolute;right:8px;bottom:4px;font-size:3.5px;color:var(--white)}
.title{position:absolute;left:12px;top:13px;font-size:7px;font-weight:700;color:var(--green-text)}
.body{position:absolute;left:12px;top:30px;width:120px;font-size:3.8px;line-height:1.6}
.body li{list-style:none}
.ph{position:absolute;border-radius:2px}
.card{background:linear-gradient(135deg,var(--purple-light),var(--purple-mid));transform:rotate(-8deg)}
.note{position:absolute;font-size:3.6px;line-height:1.4;color:#333;width:30px}
.faq p{margin-bottom:3.5px}
.faq .a{color:var(--green-text)}
.badges{position:absolute;bottom:18px;left:8px;display:flex;gap:4px}
.badges span{width:13px;height:8px;border-radius:2px;background:#d6cfc0}
.brand{font-size:7px;font-weight:600;color:var(--green-dark);display:flex;align-items:center;gap:3px}
.brand i{width:6px;height:6px;border-radius:50%;background:var(--green-pale);display:inline-block}
.pill{position:absolute;border-radius:50%;font-size:4px;display:flex;align-items:center;justify-content:center;text-align:center;color:#333;line-height:1.1}
.step{position:absolute;width:12px;height:12px;border-radius:50%;background:var(--green-dark);color:#fff;font-size:2.8px;display:flex;align-items:center;justify-content:center;text-align:center}
/* browser screenshot slides */
.browser{position:absolute;left:0;top:0;width:208px;height:140px;background:var(--chrome)}
.browser .tabs{height:5px;background:#c9ced5}
.browser .tools{height:5px;background:#eef0f3;border-bottom:1px solid #b9bec6;display:flex;align-items:center;padding-left:14px}
.browser .addr{width:70px;height:3px;background:#fff;border:.4px solid #aab}
.browser .marks{height:4px;background:#f6f7f9;border-bottom:.5px solid #ccc;display:flex;gap:3px;align-items:center;padding-left:4px}
.browser .marks span{width:14px;height:1.6px;background:#b5bac2}
.site{position:absolute;left:34px;top:14px;width:142px;height:126px;background:linear-gradient(180deg,var(--purple-light),var(--purple-mid) 85%);overflow:hidden}
.site .head{height:24px;display:flex;align-items:center;gap:4px;padding:0 6px;background:linear-gradient(90deg,#f3eef8,#e3d6ee)}
.site .logo{width:20px;height:18px;background:#a58cc6;border-radius:2px}
.site .banner{flex:1;height:18px;background:linear-gradient(90deg,#d9c9ea,#f0e8f6)}
.site .nav{height:4px;background:var(--purple);margin:0 6px;display:flex;gap:3px;padding:1px 3px}
.site .nav span{width:16px;background:#c8b2e0}
.grid{display:grid;grid-template-columns:repeat(4,1fr);gap:4px;padding:6px 10px}
.grid div{height:22px;background:#fff;border:.5px solid #c9b4de;padding:3px}
.grid div b{display:block;height:100%;background:linear-gradient(135deg,#8d8a86,#c8b89e)}
.dim{position:absolute;inset:0;background:rgba(40,30,50,.6)}
.popup{position:absolute;left:24px;top:34px;width:94px;height:52px;background:#fff;border:.5px solid #999;padding:4px;display:flex;gap:4px}
.popup b{width:34px;background:linear-gradient(135deg,#7b8f6a,#c9b08a)}
.popup p{font-size:2.6px;line-height:1.5;color:#555}
.form{margin:6px 10px;background:#fff;height:78px;padding:5px;display:flex;gap:6px}
.form b{width:24px;height:30px;background:linear-gradient(135deg,#7b8f6a,#c9b08a)}
.form .fields{flex:1;display:flex;flex-direction:column;gap:3px}
.form .fields span{height:3px;background:#e4e4ea;border:.3px solid #bbb;width:60%}
.confirm{margin:20px 24px;background:#c4dc58;height:12px;border-radius:2px;font-size:2.8px;color:#334;display:flex;align-items:center;justify-content:center}
.callout{position:absolute;font-size:3.6px;line-height:1.4;color:#333;width:30px;left:176px}
/* diagram */
.tag{position:absolute;background:var(--teal);color:#fff;font-size:3.2px;padding:.6px 2px;width:32px}
.tbl{position:absolute;border:.6px solid var(--green);background:#fff}
.tbl .cap{position:absolute;top:-4px;left:4px;background:var(--green);color:#fff;font-size:3px;padding:0 3px}
.tbl .cells{display:grid;gap:1.5px;padding:5px 3px 3px}
.tbl .cells span{font-size:2.4px;border:.4px solid var(--green-pale);background:#f6faf3;text-align:center;padding:.6px 0}
.flow{position:absolute;left:8px;top:122px;width:192px;height:9px;background:var(--green-pale);border-radius:4px;display:flex;justify-content:space-around;align-items:center}
.flow span{font-size:2.8px;font-weight:700;color:var(--green-dark);display:flex;align-items:center;gap:1px}
.flow span i{width:5px;height:5px;border-radius:50%;background:var(--teal);display:inline-block}
</style>
</head>
<body>
<svg width="0" height="0" style="position:absolute">
  <defs>
    <symbol id="footer" viewBox="0 0 208 157">
      <path d="M0 143 Q100 134 208 113 L208 157 L0 157Z" fill="var(--green-dark)"/>
      <path d="M0 140.5 Q100 131.5 208 110.5" fill="none" stroke="var(--green-pale)" stroke-width="1"/>
    </symbol>
    <symbol id="foot-flat" viewBox="0 0 208 157">
      <path d="M0 145 Q100 140 208 128 L208 157 L0 157Z" fill="var(--green-dark)"/>
    </symbol>
  </defs>
</svg>

<!-- Column 1 -->
<section class="slide c1 r1">
  <svg class="band" viewBox="0 0 208 157"><path d="M0 0 H208 V14 Q110 44 0 40Z" fill="var(--green-dark)"/><use href="#footer"/></svg>
  <div class="brand" style="position:absolute;left:14px;top:10px;color:#fff"><i></i>Rewardnest</div>
  <div style="position:absolute;left:14px;top:24px;font-size:2.8px;color:#dfeee0">Reward · Gift · Recognise · Delight</div>
  <div class="ph card" style="left:148px;top:40px;width:44px;height:30px" role="img" aria-label="Gift card with product photo"></div>
  <div class="swoosh" role="img" aria-label="Decorative curved arrows"></div>
  <div style="position:absolute;left:120px;top:80px;font-size:7.5px;font-weight:700;color:var(--purple)">Giftpicker.com</div>
  <div style="position:absolute;left:126px;top:90px;font-size:3.4px">Making Gifting Simple and Efficient</div>
  <div class="badges"><span></span><span></span><span></span><span></span><span></span></div>
  <span class="url">www.rewardnest.in</span>
</section>

<section class="slide c1 r2">
  <svg class="band" viewBox="0 0 208 157">
    <circle cx="188" cy="52" r="15" fill="var(--green-pale)" opacity=".85"/>
    <circle cx="178" cy="70" r="15" fill="var(--green-pale)" opacity=".7"/>
    <circle cx="198" cy="70" r="15" fill="var(--green)" opacity=".55"/>
    <use href="#footer"/></svg>
  <div style="position:absolute;left:178px;top:46px;font-size:2.6px;color:#fff">INNOVATE</div>
  <div class="swoosh" style="left:70px;width:100px" role="img" aria-label="Decorative curved arrows"></div>
  <div class="title">Know Us</div>
  <div class="body" style="font-size:3.3px;width:120px;line-height:1.5">Rewardnest provides marketing solutions to over 250 top corporates from various industries (i.e. Automobile, BFSI, FMCG, Pharma, Media, Retail etc.)<br><br>Through strong research and collective expertise we guide our clients in ways to help them stay connected with their people, be it their sales force, channel partners or employees.<br><br>Backed by hundreds of professionals, strong IT back bone and a wide help desk, Rewardnest has successfully navigated a number of challenges in the areas of:<br>■ Sales Incentives<br>■ Rewards and Recognition<br>■ Meetings, Events and Incentive Travel<br>■ Loyalty Marketing<br>■ Experiential Marketing</div>
  <span class="url">www.rewardnest.in</span>
</section>

<section class="slide c1 r3">
  <svg class="band" viewBox="0 0 208 157">
    <circle cx="94" cy="20" r="13" fill="var(--yellow-pale)"/>
    <path d="M74 12 H80 M74 19 H80 M74 26 H80" stroke="var(--teal)" stroke-width=".6"/>
    <path d="M148 8 V40 M148 12 H152 M148 18 H152 M148 24 H152 M148 30 H152 M148 36 H152" stroke="var(--green)" stroke-width=".5" fill="none"/>
    <path d="M70 56 L58 62 M140 56 L150 62 M104 68 V76" stroke="var(--green)" stroke-width=".5"/>
    <use href="#foot-flat"/>
  </svg>
  <div class="tag" style="left:40px;top:8px">CUSTOMERS</div>
  <div class="tag" style="left:40px;top:16px">EMPLOYEES</div>
  <div class="tag" style="left:40px;top:24px">CHANNEL PARTNERS</div>
  <div style="position:absolute;left:84px;top:15px;width:20px;text-align:center;font-size:3.6px;font-weight:700;color:var(--green-dark);line-height:1.2">YOUR<br><span style="font-size:2.4px;font-weight:400">COMPANY</span></div>
  <div style="position:absolute;left:118px;top:15px;font-size:3.6px;font-weight:700;color:var(--green-dark);line-height:1.2;text-align:center">YOUR<br><span style="font-size:2.4px;font-weight:400">ACTIVITIES</span></div>
  <div style="position:absolute;left:154px;top:8px;font-size:2.8px;line-height:2.2;color:var(--green-text)">Motivate<br>Retain<br>Acquire<br>Motivate<br>Reward</div>
  <div class="brand" style="position:absolute;left:84px;top:50px;font-size:6px"><i></i>Rewardnest</div>
  <div style="position:absolute;left:40px;top:62px;font-size:3px;font-weight:700;color:var(--green-dark)">■ PRINT</div>
  <div style="position:absolute;left:146px;top:62px;font-size:3px;font-weight:700;color:var(--green-dark)">DIGITAL ■</div>
  <div style="position:absolute;left:96px;top:77px;font-size:3px;font-weight:700;color:var(--green-dark)">■ ONLINE</div>
  <div class="tbl" style="left:18px;top:90px;width:82px;height:29px"><span class="cap">Products</span>
    <div class="cells" style="grid-template-columns:repeat(4,1fr)"><span>Travel</span><span>Lifestyle</span><span>Music</span><span>Fun Cards</span><span>Gift Cards</span><span>Gadgets</span><span>Phones</span><span>Retail</span><span>Merchandise</span><span>E-Vouchers</span><span>Loyalty</span><span>Hotels</span></div></div>
  <div class="tbl" style="left:108px;top:90px;width:84px;height:29px"><span class="cap" style="left:auto;right:4px">Solutions</span>
    <div class="cells" style="grid-template-columns:1fr 1fr"><span>Customer Loyalty</span><span>Dealer Incentives</span><span>Employee Rewards</span><span>Promotion Marketing</span></div></div>
  <div class="flow"><span><i></i>DESIGN</span><span><i></i>TECHNOLOGY</span><span><i></i>MONITOR</span><span><i></i>ENGAGE</span><span><i></i>MEASURE</span><span><i></i>DELIVER</span></div>
  <span class="url">www.rewardnest.in</span>
</section>

<section class="slide c1 r4">
  <svg class="band" viewBox="0 0 208 157"><use href="#footer"/></svg>
  <div class="swoosh" role="img" aria-label="Decorative curved arrows"></div>
  <div style="position:absolute;left:46px;top:14px;font-size:5.5px;font-weight:700;color:var(--green-text);line-height:1.3">Giftpicker<br>An excellent rewarding tool</div>
  <div class="body" style="left:42px;top:42px;width:140px;font-size:3.6px;line-height:1.7">An electronic gift voucher which offers the flexibility, choice and convenience to redeem products online. An unique hassle free quick tool compared to the traditional way of gifting. Do away with vendor negotiations, warehousing, logistics etc. Gift the voucher to your customers, employees, channel partners and also gift them the option of redeeming a product of their choice. It acts as a double benefit.</div>
  <div class="pill" style="left:28px;top:108px;width:32px;height:20px;background:#f0a3a0">USP</div>
  <div class="pill" style="left:64px;top:108px;width:32px;height:20px;background:#f3df9c">Features</div>
  <div class="pill" style="left:100px;top:106px;width:32px;height:20px;background:#c5b4e0">Website</div>
  <div class="pill" style="left:136px;top:104px;width:38px;height:22px;background:#a9d3df">Redemption<br>Process</div>
  <span class="url">www.rewardnest.in</span>
</section>

<!-- Column 2 -->
<section class="slide c2 r1">
  <svg class="band" viewBox="0 0 208 157"><use href="#footer"/></svg>
  <div class="swoosh" role="img" aria-label="Decorative curved arrows"></div>
  <div class="title" style="left:24px;top:16px;font-size:5.5px">Stands Apart</div>
  <ul class="body" style="left:20px;top:42px"><li>○ More options in single price bandwidth.</li><li style="margin-top:4px">○ Double benefit – Gift Voucher along with the freedom to choose</li></ul>
  <span class="url">www.rewardnest.in</span>
</section>

<section class="slide c2 r2">
  <svg class="band" viewBox="0 0 208 157"><use href="#footer"/></svg>
  <div class="swoosh" role="img" aria-label="Decorative curved arrows"></div>
  <div class="title" style="left:20px;color:#666;font-weight:400;font-size:5px">Why <span style="color:var(--purple);font-size:7px">giftpicker</span> ?</div>
  <div class="ph card" style="left:150px;top:20px;width:38px;height:25px" role="img" aria-label="Gift card with product photo"></div>
  <ul class="body" style="left:18px;top:33px;font-size:3.4px;width:140px"><li>- Hassle free gifting – no sourcing no storing</li><li>- Easy delivery of vouchers</li><li>- Validity of 3 months</li><li>- Wide range of products with different price bandwidth</li><li>- All vouchers coded according to the price bandwidth</li><li>- Gifts viewed on the site would be connected to the unique code on the voucher</li><li>- Branding on both the vouchers as well as on the website</li><li>- Wide choice for the end users</li><li>- Helpdesk for query management</li><li>- MIS</li></ul>
  <span class="url">www.rewardnest.in</span>
</section>

<section class="slide c2 r3">
  <svg class="band" viewBox="0 0 208 157"><use href="#footer"/></svg>
  <div class="swoosh" role="img" aria-label="Decorative curved arrows"></div>
  <div class="title" style="left:24px;font-size:6px">Website</div>
  <ul class="body" style="left:22px;top:40px;width:160px;font-size:3.4px;line-height:1.8"><li>- The gifts can be redeemed @ <u style="color:#2a4fb0">www.giftpicker.com</u></li><li>- A very user friendly website with simple click options</li><li>- Branding can be done to establish emotional connect for higher brand recall</li><li>- All the details pertaining to the products can be viewed on the site</li><li>- Customer personal details along with the address is captured which can be further used for more promotions</li></ul>
  <span class="url">www.rewardnest.in</span>
</section>

<section class="slide c2 r4">
  <svg class="band" viewBox="0 0 208 157">
    <path d="M26 88 Q30 66 58 60" fill="none" stroke="var(--green-dark)" stroke-width="1.2"/><path d="M56 57 L61 60 L56 63Z" fill="var(--green-dark)"/>
    <path d="M72 58 Q86 50 100 56" fill="none" stroke="var(--green-dark)" stroke-width="1.2"/><path d="M98 53 L103 57 L97 59Z" fill="var(--green-dark)"/>
    <path d="M112 60 Q132 66 142 82" fill="none" stroke="var(--green-dark)" stroke-width="1.2"/><path d="M139 81 L143 86 L145 80Z" fill="var(--green-dark)"/>
    <use href="#footer"/></svg>
  <div class="swoosh" style="left:110px;width:98px" role="img" aria-label="Decorative curved arrows"></div>
  <div class="title" style="left:24px;font-size:5.5px">Redemption Process</div>
  <div class="note" style="left:24px;top:36px;width:52px">Customer visits the website, <u style="color:#2a4fb0">www.giftpicker.com</u> to register the voucher</div>
  <div class="note" style="left:128px;top:40px;width:56px">Customer can view the products and redeem one of his choice</div>
  <div class="step" style="left:20px;top:90px">Step<br>1</div>
  <div class="step" style="left:62px;top:52px">Step<br>2</div>
  <div class="step" style="left:104px;top:50px">Step<br>3</div>
  <div class="step" style="left:140px;top:86px">Step<br>4</div>
  <div class="note" style="left:24px;top:110px;width:42px">Customer receives the voucher</div>
  <div class="note" style="left:138px;top:100px;width:50px">Rewardnest delivers the product to the customers address.</div>
  <span class="url">www.rewardnest.in</span>
</section>

<!-- Column 3 -->
<section class="slide c3 r1">
  <svg class="band" viewBox="0 0 208 157"><use href="#footer"/></svg>
  <div class="swoosh" role="img" aria-label="Decorative curved arrows"></div>
  <div class="title" style="left:20px;color:#666;font-size:5px">The Working</div>
  <div class="ph card" style="left:62px;top:50px;width:70px;height:34px;background:linear-gradient(135deg,#fff,#d8d0e4);border:.5px solid #bbb" role="img" aria-label="Back of gift voucher card with scratch code area"></div>
  <div class="note" style="left:150px;top:58px;width:40px">Your Unique No printed here</div>
  <span class="url">www.rewardnest.in</span>
</section>

<section class="slide c3 r2">
  <div class="browser"><div class="tabs"></div><div class="tools"><div class="addr"></div></div><div class="marks"><span></span><span></span><span></span><span></span><span></span><span></span><span></span></div>
    <div class="site" style="left:30px;width:150px">
      <div class="head"><div class="logo" role="img" aria-label="Site logo area"></div><div class="banner" role="img" aria-label="Welcome banner with model and gift boxes"></div></div>
      <div class="nav"><span></span><span></span><span></span><span></span></div>
      <div style="display:flex;gap:6px;padding:6px 8px">
        <div style="width:50px;height:40px;background:#f1eaf7;font-size:2.6px;padding:4px;color:#555">Enter your gift card number<div style="margin-top:3px;height:4px;background:#fff;border:.3px solid #aaa"></div></div>
        <div style="flex:1;height:40px;background:var(--purple);font-size:2.8px;color:#fff;padding:5px;line-height:1.5">A fantastic array of products, built to ensure we are on your side and the offer is made for you.<br><span style="color:#e8e070">Go ahead, pick a gift!</span></div>
      </div>
      <div style="display:flex;gap:4px;padding:2px 8px"><span style="width:22px;height:8px;background:#fff"></span><span style="width:22px;height:8px;background:#fff"></span><span style="width:22px;height:8px;background:#fff"></span><span style="width:22px;height:8px;background:#fff"></span></div>
    </div></div>
  <svg class="band" viewBox="0 0 208 157"><use href="#foot-flat"/></svg>
  <span class="url">www.rewardnest.in</span>
</section>

<section class="slide c3 r3">
  <div class="browser"><div class="tabs"></div><div class="tools"><div class="addr"></div></div><div class="marks"><span></span><span></span><span></span><span></span><span></span><span></span></div>
    <div class="site">
      <div class="head"><div class="logo" role="img" aria-label="Site logo area"></div><div class="banner" role="img" aria-label="Banner with model and gift boxes"></div></div>
      <div class="nav"><span></span><span></span><span></span><span></span></div>
      <div class="grid"><div><b role="img" aria-label="Product photo"></b></div><div><b role="img" aria-label="Product photo"></b></div><div style="border-color:#d33"><b role="img" aria-label="Product photo"></b></div><div><b role="img" aria-label="Product photo"></b></div><div><b role="img" aria-label="Product photo"></b></div><div><b role="img" aria-label="Product photo"></b></div><div><b role="img" aria-label="Product photo"></b></div><div><b role="img" aria-label="Product photo"></b></div></div>
    </div></div>
  <svg class="band" viewBox="0 0 208 157"><use href="#foot-flat"/></svg>
  <div class="callout" style="top:86px">Browse through the Gifts</div>
  <span class="url">www.rewardnest.in</span>
</section>

<section class="slide c3 r4">
  <div class="browser"><div class="tabs"></div><div class="tools"><div class="addr"></div></div><div class="marks"><span></span><span></span><span></span><span></span><span></span></div>
    <div class="site">
      <div class="head"><div class="logo" role="img" aria-label="Site logo area"></div><div class="banner" role="img" aria-label="Banner with model and gift boxes"></div></div>
      <div class="nav"><span></span><span></span><span></span><span></span></div>
      <div class="grid"><div><b role="img" aria-label="Product photo"></b></div><div><b role="img" aria-label="Product photo"></b></div><div><b role="img" aria-label="Product photo"></b></div><div><b role="img" aria-label="Product photo"></b></div><div><b role="img" aria-label="Product photo"></b></div><div><b role="img" aria-label="Product photo"></b></div><div><b role="img" aria-label="Product photo"></b></div><div><b role="img" aria-label="Product photo"></b></div></div>
    </div></div>
  <svg class="band" viewBox="0 0 208 157"><use href="#foot-flat"/></svg>
  <div class="callout" style="top:86px">See larger images</div>
  <span class="url">www.rewardnest.in</span>
</section>

<!-- Column 4 -->
<section class="slide c4 r1">
  <div class="browser"><div class="tabs"></div><div class="tools"><div class="addr"></div></div><div class="marks"><span></span><span></span><span></span><span></span><span></span><span></span></div>
    <div class="site">
      <div class="head"><div class="logo"></div><div class="banner"></div></div>
      <div class="grid"><div></div><div></div><div></div><div></div></div>
      <div class="dim"></div>
      <div class="popup"><b role="img" aria-label="Enlarged product photo"></b><p><strong>Product Details</strong><br>Size, colour and features of the selected gift are listed here.</p></div>
    </div></div>
  <div style="position:absolute;inset:0 0 17px 0;background:rgba(40,30,50,.45)"></div>
  <svg class="band" viewBox="0 0 208 157"><use href="#foot-flat"/></svg>
  <div class="callout" style="top:86px;color:#fff">View Details of each product</div>
  <span class="url">www.rewardnest.in</span>
</section>

<section class="slide c4 r2">
  <div class="browser"><div class="tabs"></div><div class="tools"><div class="addr"></div></div><div class="marks"><span></span><span></span><span></span><span></span><span></span><span></span></div>
    <div class="site">
      <div class="head"><div class="logo" role="img" aria-label="Site logo area"></div><div class="banner" role="img" aria-label="Banner with model"></div></div>
      <div class="nav"><span></span><span></span><span></span></div>
      <div class="form"><b role="img" aria-label="Selected product photo"></b><div class="fields"><span></span><span></span><span></span><span></span><span></span><span></span><span></span><span style="width:30%;background:var(--purple-mid)"></span></div></div>
    </div></div>
  <svg class="band" viewBox="0 0 208 157"><use href="#foot-flat"/></svg>
  <div class="callout" style="top:86px">Order for your choice of Gift - just fill in the form</div>
  <span class="url">www.rewardnest.in</span>
</section>

<section class="slide c4 r3">
  <div class="browser"><div class="tabs"></div><div class="tools"><div class="addr"></div></div><div class="marks"><span></span><span></span><span></span><span></span><span></span></div>
    <div class="site">
      <div class="head"><div class="logo" role="img" aria-label="Site logo area"></div><div class="banner" role="img" aria-label="Banner with model"></div></div>
      <div class="nav"><span></span><span></span><span></span></div>
      <div class="confirm">Thank you for using Giftpicker. Your order is confirmed.</div>
    </div></div>
  <svg class="band" viewBox="0 0 208 157"><use href="#foot-flat"/></svg>
  <div class="callout" style="top:70px">Your Order is accepted and you will receive a mail with the time of delivery.</div>
  <span class="url">www.rewardnest.in</span>
</section>

<section class="slide c4 r4">
  <svg class="band" viewBox="0 0 208 157"><use href="#footer"/></svg>
  <div class="swoosh" role="img" aria-label="Decorative curved arrows"></div>
  <div class="title" style="font-size:5.5px">FAQ's for End Users</div>
  <div class="body faq" style="top:30px;width:170px;font-size:3px;line-height:1.4">
    <p>1. How do I register the GP Card?<br><span class="a">A. Log on to www.giftpicker.com and enter the code on the card.</span></p>
    <p>2. What is the validity of the GP Card?<br><span class="a">A. The card is valid for 3 months; redeem your gift within this period.</span></p>
    <p>3. Can I redeem any product on the site?<br><span class="a">A. Yes, any product that you are able to view.</span></p>
    <p>4. Do I get a confirmation code once I finish?<br><span class="a">A. Yes, a confirmation code is mailed once done.</span></p>
    <p>5. How many days will it take for the product to reach me?<br><span class="a">A. The product will reach within 21 working days.</span></p>
    <p>6. Will I get details of the dispatch?<br><span class="a">A. Yes, dispatch details are mailed to you.</span></p>
    <p>7. Where should I call if I don't get the product?<br><span class="a">A. Call the helpdesk for any queries.</span></p>
  </div>
  <span class="url">www.rewardnest.in</span>
</section>

<!-- Column 5 -->
<section class="slide c5 r1">
  <svg class="band" viewBox="0 0 208 157"><use href="#footer"/></svg>
  <div class="swoosh" role="img" aria-label="Decorative curved arrows"></div>
  <div class="title" style="left:18px;font-size:5.5px">FAQ's for Corporates</div>
  <div class="body faq" style="left:16px;top:36px;width:150px;font-size:3px;line-height:1.4">
    <p>1. How can we distribute the GP Card to the end user?<br><span class="a">A. The card can be distributed personally or by courier.</span></p>
    <p>2. Can the GP Card be customized?<br><span class="a">A. Yes, company logos can be added on bulk orders.</span></p>
    <p>3. Can the products be decided by us?<br><span class="a">A. Yes, products can be selected if ordered in bulk.</span></p>
    <p>4. Is there a helpdesk to guide the end user?<br><span class="a">A. Yes, a Rewardnest helpdesk handles all queries.</span></p>
  </div>
  <span class="url">www.rewardnest.in</span>
</section>

<section class="slide c5 r2">
  <svg class="band" viewBox="0 0 208 157"><use href="#footer"/></svg>
  <div class="swoosh" role="img" aria-label="Decorative curved arrows"></div>
  <div style="position:absolute;left:44px;top:44px;font-size:5px;font-weight:600">For more info on this product</div>
  <div class="note" style="left:44px;top:52px;width:74px;font-size:3.2px">Contact<br>Anil Verma<br>+91 90000 12345<br><br>Rewardnest<br>12 Lakeview Road, Andheri West,<br>Mumbai 400000<br>T: +91 22 4000 0000</div>
  <div class="brand" style="position:absolute;left:130px;top:62px"><i></i>Rewardnest</div>
  <div class="badges" style="left:auto;right:60px"><span></span><span></span><span></span><span></span><span></span></div>
  <span class="url">www.rewardnest.in</span>
</section>
</body>
</html>
```